would like to incorporate logo. having business card done also. a scan code to bring patients to my website would also be great. MarcoTellerDDS.net is web site (this may be something I have to add at printing step, not sure how all that works, so don't sweat this detail)

Logo (maybe on top or upper corner)
Brightwell Crest Dental Associates (probably not necessary because it is written in logo)
Marco Teller DDS

Ossining, NY 10562
555-302-7718
(and second office)

482 N Larchmere Ave
Mt. Kisco, NY 10549
555-604-1293

Reason: partner out of town, want him to see designs to help choose

Reason: almost done choosing. just need a couple more days!!

Reason: finalizing both card and letterhead

Target Market(s)

Wealthy suburb of New York City. business executives, and their home maker wives, and families. Actors and actresses, or stage performers looking for high end cosmetic and implant dentistry, as well as family dentistry.

Industry/Entity Type

Business

Font styles to use
Serif
Script
Other font styles liked:
• open to suggestions

Colors
d3a5cc
acd037
cbdf83
b768aa

Requirements
Nice to have
• can mention fact that we have a private in house lab, so we oversee all aspects of cosmetic procedures

```html
<!DOCTYPE html>
<html lang="en">
<head>
<meta charset="utf-8">
<title>Brightwell Crest Dental Associates — Letterhead</title>
<link rel="stylesheet" href="https://fonts.googleapis.com/css2?family=Lora:wght@500&display=swap">
<style>
  :root {
    --plum: #8f2468;
    --leaf: #acd037;
    --leaf-soft: #a9c873;
    --ink: #5a4a55;
    --paper: #ffffff;
  }
  * { margin: 0; padding: 0; box-sizing: border-box; }
  html, body { width: 849px; height: 1200px; overflow: hidden; background: var(--paper); }
  .letterhead {
    position: relative;
    width: 849px;
    height: 1200px;
    background: var(--paper);
    font-family: "Lora", Georgia, serif;
    font-weight: 500;
  }
  .band { position: absolute; left: 0; width: 100%; }
  .band-top-leaf { top: 0; height: 20px; background: var(--leaf-soft); }
  .band-top-plum { top: 20px; height: 37px; background: var(--plum); }
  .band-bottom-plum { top: 1160px; height: 29px; background: var(--plum); }
  .band-bottom-leaf { top: 1189px; height: 11px; background: var(--leaf-soft); }

  .brand {
    position: absolute;
    top: 84px;
    left: 0;
    width: 100%;
    display: flex;
    justify-content: center;
    align-items: center;
    gap: 14px;
  }
  .brand-mark {
    width: 30px;
    height: 30px;
    background: var(--plum);
    flex: none;
  }
  .brand-name {
    color: var(--plum);
    font-size: 21px;
    font-weight: 500;
    letter-spacing: 3px;
    text-transform: uppercase;
    line-height: 1;
  }

  .contact {
    position: absolute;
    top: 1108px;
    left: 0;
    width: 100%;
    text-align: center;
    color: var(--ink);
    font-size: 13px;
    line-height: 20px;
  }
  .contact .sep { color: var(--plum); padding: 0 8px; }
</style>
</head>
<body>
  <main class="letterhead">
    <div class="band band-top-leaf"></div>
    <div class="band band-top-plum"></div>

    <header class="brand">
      <div class="brand-mark"></div>
      <h1 class="brand-name">Brightwell Crest Dental Associates</h1>
    </header>

    <footer class="contact">
      <p>Marco Teller DDS<span class="sep">|</span>MarcoTellerDDS.net</p>
      <p>Ossining, NY 10562 &nbsp;555-302-7718<span class="sep">|</span>482 N Larchmere Ave, Mt. Kisco, NY 10549 &nbsp;555-604-1293</p>
    </footer>

    <div class="band band-bottom-plum"></div>
    <div class="band band-bottom-leaf"></div>
  </main>
</body>
</html>
```